Logo and Business Card Design

We are macadamia farmers with a network of operations able to deliver macadamia nuts to you!
Be it wholesale or retail supply, our production capacity, network of farms and processing facilities is able to provide reliable and secure supply of macadamia products.
We have a network of owned and contract production macadamia farms located throughout Queensland and New South Wales. Our farms are located in the lush green hinterland area of Northern New south wales and the rich and productive farmlands of the Burnett area of southern Queensland. We pride ourselves on our environmentally sensitive production systems, the ownership and pride in which our network of farmers care for their orchards and the food we produce. Collectively our farms deliver to processing facilities able to provide macadamia nut in shell and kernel in wholesale and retail quantities.
Our point of difference is our integrated supply chain, delivering paddock to plate capacity.
The enterprise is a true network in that we have combined production, processing and marketing expertise into a one stop shop!
Our design should communicate our network capacity, we are a food producer which is respectful of the land and the environment in which we operate.
Our focus is Macadamia nut production, we farm and process Macadamia's where they are a native tree.

The draft design concept we feel is too mechanical and sterile, its time for something fresh and exciting!

Environment

Pell Orchard Pty. Ltd
An Integrated Macadamia production Enterprise.

```html
<!DOCTYPE html>
<html lang="en">
<head>
<meta charset="utf-8">
<title>Pell Orchard – Business Card</title>
<link rel="stylesheet" href="https://fonts.googleapis.com/css2?family=Questrial&family=Roboto+Condensed:wght@400;700&display=swap">
<style>
  :root {
    --page: #efece6;
    --green-deep: #1f4412;
    --green-mid: #3f8a1f;
    --green-bright: #63b534;
    --green-brand: #3d7d22;
    --green-icon: #6cc04a;
    --pill: #e4f2c4;
    --pattern-front: rgba(120, 190, 70, 0.30);
    --pattern-back: rgba(214, 236, 170, 0.75);
    --white: #ffffff;
    --ink: #111111;
    --husk: #86bb45;
    --husk-dark: #5e8f2a;
    --shell: #7a4a26;
    --kernel: #efe3c2;
  }
  * { box-sizing: border-box; margin: 0; padding: 0; }
  html, body {
    width: 1200px; height: 1200px; overflow: hidden;
    background: var(--page);
  }
  .canvas { position: relative; width: 1200px; height: 1200px; }

  .card {
    position: absolute; left: 172px; width: 844px; height: 521px;
    overflow: hidden;
    box-shadow: 0 4px 14px rgba(0,0,0,0.18);
  }

  /* Front */
  .card--front {
    top: 56px;
    background: radial-gradient(circle at 32% 45%, var(--green-bright) 0%, var(--green-mid) 30%, var(--green-deep) 78%, #142e0b 100%);
  }
  .front-pattern {
    position: absolute; left: 320px; top: -40px; width: 560px; height: 460px;
    background:
      radial-gradient(ellipse at 78% 28%, var(--pattern-front) 0%, rgba(120,190,70,0) 45%),
      radial-gradient(ellipse at 40% 10%, var(--pattern-front) 0%, rgba(120,190,70,0) 38%),
      radial-gradient(ellipse at 92% 62%, var(--pattern-front) 0%, rgba(120,190,70,0) 35%);
  }
  .front-brand {
    position: absolute; left: 76px; top: 208px;
    display: flex; align-items: center; gap: 16px;
  }
  .brand-dot {
    width: 30px; height: 30px; border-radius: 50%;
    background: var(--white);
  }
  .front-brand .brand-name {
    font-family: "Questrial", sans-serif;
    font-size: 62px; color: var(--white); line-height: 1;
  }
  .front-tagline {
    position: absolute; left: 76px; top: 345px;
    font-family: "Roboto Condensed", sans-serif; font-weight: 700;
    font-size: 17px; color: var(--white); letter-spacing: 0.3px;
  }
  .nut-photo {
    position: absolute; left: 440px; top: 215px; width: 330px; height: 265px;
    border-radius: 50%;
    background:
      radial-gradient(ellipse at 62% 30%, var(--husk) 0%, var(--husk-dark) 28%, rgba(94,143,42,0) 52%),
      radial-gradient(ellipse at 30% 62%, var(--shell) 0%, rgba(122,74,38,0.6) 22%, rgba(122,74,38,0) 42%),
      radial-gradient(ellipse at 40% 78%, var(--kernel) 0%, rgba(239,227,194,0) 16%),
      radial-gradient(ellipse at 50% 50%, rgba(94,143,42,0.55) 0%, rgba(94,143,42,0) 70%);
  }

  /* Back */
  .card--back { top: 607px; background: var(--white); }
  .back-pattern {
    position: absolute; left: 0; top: 0; width: 480px; height: 521px;
    background:
      radial-gradient(ellipse at 20% 88%, var(--pattern-back) 0%, rgba(214,236,170,0) 32%),
      radial-gradient(ellipse at 58% 92%, var(--pattern-back) 0%, rgba(214,236,170,0) 28%),
      radial-gradient(ellipse at 62% 12%, var(--pattern-back) 0%, rgba(214,236,170,0) 26%),
      radial-gradient(ellipse at 8% 40%, var(--pattern-back) 0%, rgba(214,236,170,0) 26%);
  }
  .back-brand {
    position: absolute; left: 46px; top: 182px;
    display: flex; align-items: center; gap: 14px;
  }
  .back-brand .brand-dot { background: var(--green-brand); width: 26px; height: 26px; }
  .back-brand .brand-name {
    font-family: "Questrial", sans-serif;
    font-size: 52px; color: var(--green-brand); line-height: 1;
  }
  .person-name {
    position: absolute; left: 553px; top: 98px;
    font-family: "Roboto Condensed", sans-serif; font-weight: 400;
    font-size: 58px; color: var(--ink); letter-spacing: -1px;
  }
  .contact-list { list-style: none; }
  .contact-row {
    position: absolute; left: 389px; right: 2px;
    display: flex; align-items: center; justify-content: flex-end;
    padding-right: 32px; gap: 52px;
    background: var(--pill);
    border-radius: 22px 0 0 22px;
    font-family: "Questrial", sans-serif; font-size: 19px; color: var(--ink);
    text-align: right;
  }
  .contact-row--phone { top: 195px; height: 58px; }
  .contact-row--address { top: 268px; height: 66px; font-size: 16px; line-height: 1.3; }
  .contact-row--email { top: 348px; height: 62px; }
  .contact-row--web { top: 425px; height: 64px; }
  .contact-icon { width: 30px; height: 30px; flex: none; fill: var(--green-icon); }
</style>
</head>
<body>
<main class="canvas">

  <section class="card card--front" aria-label="Card front">
    <div class="front-pattern" role="img" aria-label="Faint network pattern of rings joined by lines"></div>
    <div class="front-brand">
      <span class="brand-dot"></span>
      <span class="brand-name">Pell Orchard</span>
    </div>
    <p class="front-tagline">An Integrated Macadamia Production Enterprise</p>
    <div class="nut-photo" role="img" aria-label="Photo of whole and cracked macadamia nuts in green husks"></div>
  </section>

  <section class="card card--back" aria-label="Card back">
    <div class="back-pattern" role="img" aria-label="Pale network pattern of rings joined by lines"></div>
    <div class="back-brand">
      <span class="brand-dot"></span>
      <span class="brand-name">Pell Orchard</span>
    </div>
    <h1 class="person-name">Ada Merrin</h1>
    <ul class="contact-list">
      <li class="contact-row contact-row--phone">
        <span>1800-55XX-XXX</span>
        <svg class="contact-icon" viewBox="0 0 24 24" aria-hidden="true"><path d="M6.6 10.8a15 15 0 0 0 6.6 6.6l2.2-2.2a1 1 0 0 1 1-.25 11.4 11.4 0 0 0 3.6.57 1 1 0 0 1 1 1V20a1 1 0 0 1-1 1A17 17 0 0 1 3 4a1 1 0 0 1 1-1h3.5a1 1 0 0 1 1 1c0 1.25.2 2.45.57 3.57a1 1 0 0 1-.25 1z"/></svg>
      </li>
      <li class="contact-row contact-row--address">
        <span>8 B- RIDGE ROAD<br>ORCHARD ZONE, QL 45210</span>
        <svg class="contact-icon" viewBox="0 0 24 24" aria-hidden="true"><path d="M12 2 1 12h3v10h6v-6h4v6h6V12h3z"/></svg>
      </li>
      <li class="contact-row contact-row--email">
        <span>hello@pellorchard.com</span>
        <svg class="contact-icon" viewBox="0 0 24 24" aria-hidden="true"><path d="M1 5h22v14H1z M1 5l11 8 11-8" stroke="#fff" stroke-width="1.4"/></svg>
      </li>
      <li class="contact-row contact-row--web">
        <span>www.pellorchard.au</span>
        <svg class="contact-icon" viewBox="0 0 24 24" aria-hidden="true"><circle cx="12" cy="12" r="11"/><path d="M1 12h22M12 1c4 4 4 18 0 22M12 1c-4 4-4 18 0 22" stroke="#fff" stroke-width="1.3" fill="none"/></svg>
      </li>
    </ul>
  </section>

</main>
</body>
</html>
```